Business card design for new brand

We have recently rebranded and need a new business card template.

We are an insurance underwriting agency. All of our products are sold via other partner companies, so these are just to pass on our details to other organisations.

We would like to see designs that use the colour green (current stationary generally uses lime green (rgb 142,190,63) and forest green (0,154,79) to comply with our logo's colours. We are happy with other shades of green.

Business cards need to include our logo, as well as space for:
1. Full name
2. Qualifications (optional)
3. Title
4. Office number
5. Mobile number
6. Email address

Our logo is enclosed here.

```html
<!DOCTYPE html>
<html lang="en">
<head>
<meta charset="utf-8">
<title>Fernwell Business Card</title>
<link rel="stylesheet" href="https://fonts.googleapis.com/css2?family=Oswald:wght@500&family=Montserrat:wght@500;600&family=Exo+2:wght@400&display=swap">
<style>
  :root {
    --backdrop: #7a7a7a;
    --forest: #025c2a;
    --forest-bright: #0a9a40;
    --lime: #c8d400;
    --lime-band: #b5cf1f;
    --white: #ffffff;
    --ink: #111111;
  }
  * { margin: 0; padding: 0; box-sizing: border-box; }
  html, body {
    width: 1200px; height: 1200px; overflow: hidden;
    background: var(--backdrop);
  }
  .card {
    position: absolute; left: 262px;
    width: 686px; height: 392px;
    overflow: hidden;
  }
  .card-front { top: 165px; background: var(--forest); }
  .card-back { top: 653px; }
  .front-shape { position: absolute; inset: 0; }
  .holder { position: absolute; left: 29px; top: 115px; }
  .holder-name {
    font-family: "Oswald", sans-serif; font-weight: 500;
    font-size: 27px; line-height: 1; color: var(--lime);
    letter-spacing: 0.2px;
  }
  .holder-title {
    font-family: "Montserrat", sans-serif; font-weight: 600;
    font-size: 16px; color: var(--white); margin-top: 4px;
  }
  .contact-list { list-style: none; margin-top: 24px; }
  .contact-list li {
    display: flex; align-items: center; gap: 10px;
    font-family: "Montserrat", sans-serif; font-weight: 600;
    font-size: 15.5px; color: var(--white); height: 20px;
  }
  .contact-list svg { width: 13px; height: 13px; flex: none; }
  .brand {
    position: absolute; left: 372px; top: 182px;
    display: flex; align-items: center; gap: 14px;
  }
  .brand-square { width: 30px; height: 30px; background: var(--forest-bright); }
  .brand-name {
    font-family: "Exo 2", sans-serif; font-weight: 400;
    color: var(--ink); line-height: 1;
  }
  .brand-name .main { display: block; font-size: 42px; }
  .brand-name .sub { display: block; font-size: 20px; margin-top: 4px; padding-left: 32px; }
  .back-pattern {
    position: absolute; inset: 0;
    background: linear-gradient(90deg, #13a948 0%, #0b8a3a 40%, #04592a 70%, #02361a 100%);
  }
  .back-brand {
    position: absolute; left: 522px; top: 285px;
    font-family: "Exo 2", sans-serif; font-weight: 400;
    font-size: 22px; color: var(--white);
  }
</style>
</head>
<body>
  <section class="card card-front">
    <svg class="front-shape" viewBox="0 0 686 392" aria-hidden="true">
      <polygon points="445,0 686,0 686,392 428,392 261,289 261,100" fill="var(--white)"/>
      <polygon points="440,0 452,0 277,104 277,286 268,281 268,104" fill="var(--lime-band)"/>
      <polygon points="261,289 268,283 430,384 428,392" fill="var(--forest-bright)"/>
      <polygon points="268,283 277,286 444,392 430,392" fill="var(--forest-bright)"/>
    </svg>

    <div class="holder">
      <h1 class="holder-name">DANIEL HARTLEY</h1>
      <p class="holder-title">President</p>
      <ul class="contact-list">
        <li>
          <svg viewBox="0 0 24 24"><path fill="var(--lime)" d="M6.6 10.8a15 15 0 0 0 6.6 6.6l2.2-2.2c.3-.3.7-.4 1-.2 1.1.4 2.3.6 3.6.6.6 0 1 .4 1 1V20c0 .6-.4 1-1 1A17 17 0 0 1 3 4c0-.6.4-1 1-1h3.5c.6 0 1 .4 1 1 0 1.3.2 2.5.6 3.6.1.3 0 .7-.2 1z"/></svg>
          402-118-7731
        </li>
        <li>
          <svg viewBox="0 0 24 24"><rect x="6" y="2" width="12" height="20" rx="2" fill="none" stroke="var(--lime)" stroke-width="2.5"/><rect x="10" y="17" width="4" height="2" fill="var(--lime)"/></svg>
          402-655-1904
        </li>
        <li>
          <svg viewBox="0 0 24 24"><rect x="2" y="5" width="20" height="14" fill="var(--lime)"/><path d="M2 5l10 8 10-8" fill="none" stroke="var(--forest)" stroke-width="2"/></svg>
          hello@fernwell.com
        </li>
        <li>
          <svg viewBox="0 0 24 24"><circle cx="12" cy="12" r="10" fill="var(--lime)"/><path d="M2 12h20M12 2c3 3 3 17 0 20M12 2c-3 3-3 17 0 20" fill="none" stroke="var(--forest)" stroke-width="1.5"/></svg>
          www.fernwell.com
        </li>
      </ul>
    </div>

    <div class="brand">
      <span class="brand-square"></span>
      <p class="brand-name"><span class="main">Fernwell</span><span class="sub">Australia Pty Ltd</span></p>
    </div>
  </section>

  <section class="card card-back">
    <div class="back-pattern" role="img" aria-label="Repeating embossed brand pattern in green tones, bright on the left fading to deep forest green on the right"></div>
    <p class="back-brand">Fernwell</p>
  </section>
</body>
</html>
```